Design our beautiful and attractive PowerPoint template presentation

As you can see in the files attached below within this brief, we would like pls to receive a proposal for our Ravlo Drive Systems a powerpoint template which would include:
- open slide
- agenda slide
- 5 different main chapter slides , for examples below but chapter name shall be replaced according to need:
* about us
* products
* applications
* technical specifications
* testing and benchmark
- Q&A slide
- Conclusion slide
- Closing side
Pls also take a look to the web site being developed (under construction) to ensure you keep the same look and feel: http://rvdsx.pelmaro.example/index.php?id=308

Target Market(s)

Industry, multi channels

Industry/Entity Type

B-t-B mechanical parts distributors

Font styles to use
Other font styles liked:
• Pls see the font provided into the brief attached files

Requirements
Must have
• Follow the color, font and logo provided into the brief attached files
Nice to have
• Animated slides

```html
<!DOCTYPE html>
<html lang="en">
<head>
<meta charset="utf-8">
<title>Ravlo Drive Systems – Presentation Template Overview</title>
<link href="https://fonts.googleapis.com/css2?family=Montserrat:wght@400;500;600;700;800&display=swap" rel="stylesheet">
<style>
:root{
  --blue:#0b6fc2;
  --blue-deep:#0a3d73;
  --sky:#1da6ea;
  --ink:#1f1f1f;
  --grey:#6d6d6d;
  --grey-mid:#5b5b5b;
  --grey-light:#c8c8c8;
  --charcoal:#262626;
  --sheet:#e3e3e3;
  --white:#fff;
}
*{box-sizing:border-box;margin:0;padding:0}
html,body{width:703px;height:1200px;overflow:hidden;background:var(--sheet)}
body{position:relative;font-family:"Montserrat",Arial,sans-serif;color:var(--ink)}
.slide{position:absolute;width:226px;height:125px;background:var(--white);overflow:hidden}
.c1{left:7px}.c2{left:238px}.c3{left:470px}
.r1{top:7px}.r2{top:139px}.r3{top:271px}.r4{top:404px}.r5{top:536px}.r6{top:669px}.r7{top:801px}.r8{top:933px}.r9{top:1066px}

/* shared parts */
.brand{position:absolute;font-weight:800;color:var(--blue);font-size:7px;letter-spacing:.2px}
.brand.light{color:var(--white)}
.brand.corner{right:6px;top:6px;font-size:6px}
.slide-title{position:absolute;left:0;right:0;top:9px;text-align:center;font-size:8.4px;font-weight:600}
.slide-sub{position:absolute;left:0;right:0;top:19px;text-align:center;font-size:2.6px;letter-spacing:1px;color:var(--blue)}
.title-rule{position:absolute;left:108px;top:23px;width:10px;height:1.3px;background:var(--blue)}
.footer{position:absolute;left:7px;bottom:4px;width:205px;height:3.5px;background:var(--blue);font-size:1.8px;color:var(--white);padding-left:56px;line-height:3.5px;letter-spacing:.4px}
.footer-num{position:absolute;right:7px;bottom:4px;width:11px;height:3.5px;background:var(--grey-mid);font-size:1.8px;color:var(--white);text-align:center;line-height:3.5px}
.tiny{font-size:2.6px;line-height:1.35;color:var(--grey)}
.photo{position:absolute}
.cover-title{position:absolute;font-weight:700;font-size:14px;line-height:13px;color:var(--white)}
.cover-sub{position:absolute;font-size:5px;color:var(--white)}
.presented{position:absolute;font-size:3px;letter-spacing:1.2px;color:var(--white);text-align:center}
.presented b{display:block;letter-spacing:.3px;font-weight:600}
.social{position:absolute;display:flex;gap:1.5px}
.social i{width:4.5px;height:4.5px;border:.5px solid var(--white);border-radius:50%}
.chip{position:absolute;width:12px;height:12px;border-radius:50%;background:var(--blue)}
</style>
</head>
<body>

<!-- 1: cover, dark -->
<section class="slide c1 r1">
  <div class="brand" style="left:100px;top:4px">Ravlo</div>
  <div class="photo" role="img" aria-label="Dark industrial photo of a drive belt on machinery" style="left:0;top:17px;width:226px;height:108px;background:linear-gradient(110deg,#1a2836,#0d2a45 55%,#0a1e33)"></div>
  <div class="cover-title" style="left:0;right:0;top:46px;text-align:center">Presentation<br>Title Goes Here</div>
  <div class="cover-sub" style="left:0;right:0;top:76px;text-align:center">Sub Title Goes Here</div>
  <div class="presented" style="left:0;right:0;top:94px">PRESENTED BY<b>Presenter name</b></div>
  <div class="social" style="left:104px;top:105px"><i></i><i></i><i></i></div>
</section>

<!-- 2: cover, blue photo -->
<section class="slide c2 r1">
  <div class="photo" role="img" aria-label="Blue tinted photo of engineers working in a control room" style="inset:0;background:linear-gradient(120deg,#0b3f78,#1672c0 50%,#0d4f95)"></div>
  <div class="brand light" style="left:100px;top:31px">Ravlo</div>
  <div class="cover-title" style="left:0;right:0;top:46px;text-align:center">Presentation<br>Title Goes Here</div>
  <div class="cover-sub" style="left:0;right:0;top:76px;text-align:center">Sub Title Goes Here</div>
  <div class="presented" style="left:0;right:0;top:94px">PRESENTED BY<b>Presenter name</b></div>
  <div class="social" style="left:104px;top:105px"><i></i><i></i><i></i></div>
</section>

<!-- 3: cover, blue gradient -->
<section class="slide c3 r1">
  <div class="photo" role="img" aria-label="Blue gradient industrial photo with glowing light" style="inset:0;background:linear-gradient(120deg,#0a56a8,#2d7fcf 55%,#a9b7c8 85%,#e8c7a0)"></div>
  <div class="brand light" style="left:16px;top:38px">Ravlo</div>
  <div class="cover-title" style="left:15px;top:55px">Presentation<br>Title Goes Here</div>
  <div class="cover-sub" style="left:16px;top:82px">Sub Title Goes Here</div>
  <div class="presented" style="left:16px;top:101px;text-align:left">PRESENTED BY<b>Presenter name</b></div>
</section>

<!-- 4: cover, white -->
<section class="slide c1 r2">
  <div class="brand" style="left:12px;top:36px">Ravlo</div>
  <div class="cover-title" style="left:12px;top:52px;color:var(--ink)">Presentation<br>Title Goes Here</div>
  <div class="cover-sub" style="left:12px;top:79px;color:var(--grey)">Sub Title Goes Here</div>
  <div style="position:absolute;left:12px;top:102px;font-size:3.6px;color:var(--blue)">www.rvdsx.pelmaro.example</div>
  <div style="position:absolute;left:162px;top:54px;width:22px;height:22px;border-radius:50%;background:var(--grey-light)"></div>
</section>

<!-- 5: cover, charcoal -->
<section class="slide c2 r2" style="background:var(--charcoal)">
  <div class="brand" style="left:12px;top:36px">Ravlo</div>
  <div class="cover-title" style="left:12px;top:52px">Presentation<br>Title Goes Here</div>
  <div class="cover-sub" style="left:12px;top:79px">Sub Title Goes Here</div>
  <div style="position:absolute;left:12px;top:102px;font-size:3.6px;color:var(--blue)">www.rvdsx.pelmaro.example</div>
  <div style="position:absolute;left:162px;top:54px;width:22px;height:22px;border-radius:50%;background:var(--grey-light)"></div>
</section>

<!-- 6: page break -->
<section class="slide c3 r2">
  <div class="photo" role="img" aria-label="Blue tinted photo of a businessman holding a belt" style="inset:0;background:linear-gradient(120deg,#1b5fae,#4a8ed6 50%,#1f64b3)"></div>
  <div class="brand light" style="right:8px;top:76px">Ravlo</div>
  <div style="position:absolute;right:8px;top:88px;font-size:15px;font-weight:700;color:var(--white)">PAGE BREAK</div>
  <div style="position:absolute;right:8px;top:106px;font-size:4px;color:var(--white)">Sub title goes here</div>
</section>

<!-- 7: agenda -->
<section class="slide c1 r3">
  <div style="position:absolute;left:20px;top:44px;font-size:8px;font-weight:600;line-height:10px;color:var(--blue)">Here Goes<br>Title Of Your<br>Agenda</div>
  <div style="position:absolute;left:20px;top:76px;font-size:3.6px;font-weight:600">Here Goes A Short Subtitle</div>
  <ol style="position:absolute;left:120px;top:20px;width:82px;list-style:none;font-size:3.5px">
    <li style="border-bottom:.4px solid #ddd;padding:2.2px 0"><span style="display:inline-block;width:14px;color:var(--grey)">i.</span>Introduction</li>
    <li style="border-bottom:.4px solid #ddd;padding:2.2px 0"><span style="display:inline-block;width:14px;color:var(--grey)">ii.</span>About Us</li>
    <li style="border-bottom:.4px solid #ddd;padding:2.2px 0"><span style="display:inline-block;width:14px;color:var(--grey)">iii.</span>Welcome Message</li>
    <li style="border-bottom:.4px solid #ddd;padding:2.2px 0"><span style="display:inline-block;width:14px;color:var(--grey)">iv.</span>Company Profile</li>
    <li style="border-bottom:.4px solid #ddd;padding:2.2px 0"><span style="display:inline-block;width:14px;color:var(--grey)">v.</span>Team</li>
    <li style="border-bottom:.4px solid #ddd;padding:2.2px 0"><span style="display:inline-block;width:14px;color:var(--grey)">vi.</span>Team Group</li>
    <li style="border-bottom:.4px solid #ddd;padding:2.2px 0"><span style="display:inline-block;width:14px;color:var(--grey)">vii.</span>Portfolio</li>
    <li style="border-bottom:.4px solid #ddd;padding:2.2px 0"><span style="display:inline-block;width:14px;color:var(--grey)">viii.</span>Info graphic</li>
    <li style="border-bottom:.4px solid #ddd;padding:2.2px 0"><span style="display:inline-block;width:14px;color:var(--grey)">ix.</span>Contact Us</li>
  </ol>
  <div class="footer">COPYRIGHT © 2021 | Ravlo Drive Systems</div><div class="footer-num">7</div>
</section>

<!-- 8: about us -->
<section class="slide c2 r3">
  <div style="position:absolute;left:8px;top:17px;font-size:8.5px;font-weight:600">About Us</div>
  <p class="tiny" style="position:absolute;left:8px;top:34px;width:100px">Ravlo Drive Systems designs, produces and distributes quality power transmission parts for industrial use.</p>
  <div style="position:absolute;left:8px;top:52px;width:100px">
    <p style="font-size:2.8px;font-weight:700;color:var(--blue);padding-left:16px">Reliable Alternative</p>
    <p class="tiny" style="padding-left:16px">A solid option that meets strict quality and service needs.</p>
    <p style="font-size:2.8px;font-weight:700;color:var(--blue);padding-left:16px;margin-top:6px">Smart Products</p>
    <p class="tiny" style="padding-left:16px">A wide range of belts built for demanding machines.</p>
    <p style="font-size:2.8px;font-weight:700;color:var(--blue);padding-left:16px;margin-top:6px">Trustable Experience</p>
    <p class="tiny" style="padding-left:16px">Decades of field knowledge backing every order placed.</p>
  </div>
  <div class="photo" role="img" aria-label="Photo of an engineer inspecting a drive belt" style="left:113px;top:0;width:113px;height:125px;background:linear-gradient(160deg,#0a4c90,#1a78c9 60%,#cfd9e2)"></div>
</section>

<!-- 9: two columns -->
<section class="slide c3 r3">
  <div class="brand corner">Ravlo</div>
  <div class="slide-title">Here Goes Title Of This Slide</div>
  <div class="slide-sub">HERE IS A PLACE FOR SUBTITLE</div><div class="title-rule"></div>
  <p class="tiny" style="position:absolute;left:15px;top:40px;width:93px;color:var(--ink)">Lorem ipsum dolor sit amet, consectetur adipiscing elit, sed do eiusmod tempor incididunt ut labore et dolore magna aliqua. Ut enim ad minim veniam, quis nostrud exercitation ullamco laboris.</p>
  <p class="tiny" style="position:absolute;left:118px;top:40px;width:93px;color:var(--ink)">Lorem ipsum dolor sit amet, consectetur adipiscing elit, sed do eiusmod tempor incididunt ut labore et dolore magna aliqua. Ut enim ad minim veniam, quis nostrud exercitation ullamco laboris.</p>
  <ul class="tiny" style="position:absolute;left:15px;top:76px;width:93px;list-style:none;color:var(--ink)">
    <li style="margin-bottom:3px"><span style="color:var(--blue)">●</span> Lorem ipsum dolor sit amet</li>
    <li style="margin-bottom:3px"><span style="color:var(--blue)">●</span> Sed do eiusmod tempor incididunt</li>
    <li style="margin-bottom:3px"><span style="color:var(--blue)">●</span> Dolore magna aliqua enim</li>
    <li><span style="color:var(--blue)">●</span> Quis nostrud exercitation ullamco</li>
  </ul>
  <ul class="tiny" style="position:absolute;left:118px;top:76px;width:93px;list-style:none;color:var(--ink)">
    <li style="margin-bottom:3px"><span style="color:var(--blue)">●</span> Lorem ipsum dolor sit amet</li>
    <li style="margin-bottom:3px"><span style="color:var(--blue)">●</span> Sed do eiusmod tempor incididunt</li>
    <li style="margin-bottom:3px"><span style="color:var(--blue)">●</span> Dolore magna aliqua enim</li>
    <li><span style="color:var(--blue)">●</span> Quis nostrud exercitation ullamco</li>
  </ul>
  <div class="footer">COPYRIGHT © 2021 | Ravlo Drive Systems</div><div class="footer-num">9</div>
</section>

<!-- 10: product images -->
<section class="slide c1 r4">
  <div class="brand corner">Ravlo</div>
  <div class="slide-title">Here Goes Title Of This Slide</div>
  <div class="slide-sub">HERE IS A PLACE FOR SUBTITLE</div><div class="title-rule"></div>
  <div class="photo" role="img" aria-label="Photo of a white round belt" style="left:10px;top:48px;width:62px;height:40px;background:linear-gradient(#f2f2f2,#dcdcdc);border-radius:40%"></div>
  <div class="photo" role="img" aria-label="Photo of a white timing belt sleeve" style="left:83px;top:45px;width:34px;height:46px;background:linear-gradient(90deg,#dfe6ee,#f6f6f6,#e4e4e4)"></div>
  <div class="photo" role="img" aria-label="Photo of red and grey V-belts" style="left:128px;top:52px;width:30px;height:38px;background:linear-gradient(#eadcd9,#d8d8d8);border-radius:40%"></div>
  <div class="photo" role="img" aria-label="Photo of a wide white flat belt" style="left:166px;top:60px;width:44px;height:24px;background:linear-gradient(#efefef,#d6d6d6);border-radius:6px"></div>
  <div class="footer">COPYRIGHT © 2021 | Ravlo Drive Systems</div><div class="footer-num">10</div>
</section>

<!-- 11: technical specs, left image -->
<section class="slide c2 r4">
  <div class="photo" role="img" aria-label="Photo of black wrapped V-belts" style="left:2px;top:28px;width:95px;height:82px;background:radial-gradient(circle at 60% 50%,#3a3a3a,#111 70%,#fff 71%)"></div>
  <div style="position:absolute;left:107px;top:25px;font-size:8.2px;font-weight:600">Technical Specifications</div>
  <div style="position:absolute;left:107px;top:36px;font-size:2.6px;letter-spacing:1px;color:var(--grey)">CLASSICAL WRAPPED V-BELTS</div>
  <div style="position:absolute;left:107px;top:52px;font-size:5px;font-weight:600;color:var(--blue)">Features</div>
  <p class="tiny" style="position:absolute;left:107px;top:61px;width:102px">This belt has an insulation filler that gives strong grip between the cords and rubber base. The wrapping cover resists abrasion and adds grip. Meets antistatic rules. Contact us to match your specific belt need.</p>
  <div class="footer">COPYRIGHT © 2021 | Ravlo Drive Systems</div><div class="footer-num">11</div>
</section>

<!-- 12: technical specs, right image -->
<section class="slide c3 r4">
  <div style="position:absolute;left:12px;top:21px;font-size:8.2px;font-weight:600">Technical Specifications</div>
  <div style="position:absolute;left:12px;top:32px;font-size:2.6px;letter-spacing:1px;color:var(--grey)">THERMOWELDABLE SMOOTH AND ROUGH ROUND</div>
  <div style="position:absolute;left:12px;top:47px;font-size:5px;font-weight:600;color:var(--blue)">Features</div>
  <p class="tiny" style="position:absolute;left:12px;top:56px;width:110px">Our medium hard extruded belt is made of quality PU for grip and resistance to abrasion and tearing.<br>• Smooth surface, low friction on steel<br>• Hardness 85–88 Shore A<br>• Resistant to oil, fuels and oxygen<br>• Plasticizer free<br>This PU belt is weldable for light conveying uses.</p>
  <div class="photo" role="img" aria-label="Photo of a coil of green round belt with a tag" style="left:140px;top:22px;width:86px;height:88px;background:linear-gradient(135deg,#2da84a,#137a2d);border-radius:40% 0 0 40%"></div>
  <div class="footer">COPYRIGHT © 2021 | Ravlo Drive Systems</div><div class="footer-num">12</div>
</section>

<!-- 13: applications ring -->
<section class="slide c1 r5">
  <svg width="226" height="125" viewBox="0 0 226 125" style="position:absolute;left:0;top:0" font-family="Montserrat, sans-serif" font-size="4" fill="#333">
    <circle cx="113" cy="59" r="48" fill="none" stroke="#0b6fc2" stroke-width="2"/>
    <g fill="#fff" stroke="#0b6fc2" stroke-width=".8">
      <circle cx="113" cy="11" r="4.2"/><circle cx="131.4" cy="14.6" r="4.2"/><circle cx="146.9" cy="25.1" r="4.2"/><circle cx="157.4" cy="40.6" r="4.2"/>
      <circle cx="161" cy="59" r="4.2"/><circle cx="157.4" cy="77.4" r="4.2"/><circle cx="146.9" cy="92.9" r="4.2"/><circle cx="131.4" cy="103.4" r="4.2"/>
      <circle cx="113" cy="107" r="4.2"/><circle cx="94.6" cy="103.4" r="4.2"/><circle cx="79.1" cy="92.9" r="4.2"/><circle cx="68.6" cy="77.4" r="4.2"/>
      <circle cx="65" cy="59" r="4.2"/><circle cx="68.6" cy="40.6" r="4.2"/><circle cx="79.1" cy="25.1" r="4.2"/><circle cx="94.6" cy="14.6" r="4.2"/>
    </g>
    <text x="113" y="5" text-anchor="middle">Agriculture</text>
    <text x="137" y="12">Appliances</text><text x="153" y="24">Cement</text><text x="164" y="42">Tiles</text>
    <text x="167" y="61">Fitness</text><text x="164" y="80">Gardening</text><text x="153" y="95">Linear Guiding</text>
    <text x="137" y="107">Wood</text><text x="118" y="115">Food</text><text x="96" y="113" text-anchor="end">Logistic</text>
    <text x="73" y="96" text-anchor="end">Mining</text><text x="62" y="80" text-anchor="end">Packaging</text><text x="59" y="61" text-anchor="end">Paper</text>
    <text x="62" y="42" text-anchor="end">Recycling</text><text x="73" y="27" text-anchor="end">Technology</text><text x="89" y="14" text-anchor="end">Textile</text>
    <text x="113" y="50" text-anchor="middle" font-size="6.5" font-weight="600" fill="#0b6fc2">APPLICATIONS</text>
    <text x="113" y="58" text-anchor="middle">Belt that delivers high power</text>
    <text x="113" y="63" text-anchor="middle">ratings in all weathers</text>
    <text x="113" y="68" text-anchor="middle">conditions; extremely reliable</text>
    <text x="113" y="73" text-anchor="middle">for all applications.</text>
  </svg>
  <div class="footer">COPYRIGHT © 2021 | Ravlo Drive Systems</div><div class="footer-num">13</div>
</section>

<!-- 14: our products -->
<section class="slide c2 r5">
  <div style="position:absolute;left:0;top:0;width:226px;height:72px;background:var(--blue)"></div>
  <div style="position:absolute;left:0;right:0;top:10px;text-align:center;font-size:11px;font-weight:600;color:var(--white)">Our Products</div>
  <p class="tiny" style="position:absolute;left:30px;right:30px;top:28px;text-align:center;color:var(--white)">Ravlo Drive Systems designs and produces high quality drive belts in five families, built to strict standards for industrial and farm use, from first fit to spare parts.</p>
  <div class="photo" role="img" aria-label="Timing belt photo" style="left:17px;top:53px;width:28px;height:28px;border-radius:50%;background:linear-gradient(135deg,#7a4a1e,#222);border:1px solid #fff"></div>
  <div class="photo" role="img" aria-label="Thermoweldable belts photo" style="left:59px;top:53px;width:28px;height:28px;border-radius:50%;background:linear-gradient(135deg,#c44,#2a8a45);border:1px solid #fff"></div>
  <div class="photo" role="img" aria-label="Agri-belts photo" style="left:101px;top:53px;width:28px;height:28px;border-radius:50%;background:linear-gradient(135deg,#e9e2d0,#b8a98b);border:1px solid #fff"></div>
  <div class="photo" role="img" aria-label="V-belts photo" style="left:142px;top:53px;width:28px;height:28px;border-radius:50%;background:linear-gradient(135deg,#f2f2f2,#333);border:1px solid #fff"></div>
  <div class="photo" role="img" aria-label="Ribbed belts photo" style="left:183px;top:53px;width:28px;height:28px;border-radius:50%;background:linear-gradient(135deg,#c8d43a,#111 60%);border:1px solid #fff"></div>
  <div style="position:absolute;left:7px;top:86px;width:212px;display:flex;justify-content:space-between;text-align:center;font-size:2.8px;font-weight:700">
    <div style="width:40px">Timing Belts<p class="tiny" style="font-weight:400">Short sample text for this belt family here.</p></div>
    <div style="width:40px">Thermoweldable Belts<p class="tiny" style="font-weight:400">Short sample text for this belt family here.</p></div>
    <div style="width:40px">Agri-Belts<p class="tiny" style="font-weight:400">Short sample text for this belt family here.</p></div>
    <div style="width:40px">V-Belts<p class="tiny" style="font-weight:400">Short sample text for this belt family here.</p></div>
    <div style="width:40px">Ribbed Belts<p class="tiny" style="font-weight:400">Short sample text for this belt family here.</p></div>
  </div>
  <div class="footer">COPYRIGHT © 2021 | Ravlo Drive Systems</div><div class="footer-num">14</div>
</section>

<!-- 15: six items -->
<section class="slide c3 r5">
  <div class="brand corner">Ravlo</div>
  <div class="slide-title">Here Goes Title Of This Slide</div>
  <div class="slide-sub">HERE IS A PLACE FOR SUBTITLE</div><div class="title-rule"></div>
  <div class="chip" style="left:20px;top:39px"></div><div class="chip" style="left:20px;top:63px"></div><div class="chip" style="left:20px;top:87px"></div>
  <div class="chip" style="left:118px;top:39px"></div><div class="chip" style="left:118px;top:63px"></div><div class="chip" style="left:118px;top:87px"></div>
  <div style="position:absolute;left:37px;top:38px;width:62px;font-size:2.8px;font-weight:700">Project name<p class="tiny" style="font-weight:400">Lorem ipsum dolor sit amet, nec an dictas equidem appellantur.</p></div>
  <div style="position:absolute;left:37px;top:62px;width:62px;font-size:2.8px;font-weight:700">Project name<p class="tiny" style="font-weight:400">Lorem ipsum dolor sit amet, nec an dictas equidem appellantur.</p></div>
  <div style="position:absolute;left:37px;top:86px;width:62px;font-size:2.8px;font-weight:700">Project name<p class="tiny" style="font-weight:400">Lorem ipsum dolor sit amet, nec an dictas equidem appellantur.</p></div>
  <div style="position:absolute;left:135px;top:38px;width:62px;font-size:2.8px;font-weight:700">Project name<p class="tiny" style="font-weight:400">Lorem ipsum dolor sit amet, nec an dictas equidem appellantur.</p></div>
  <div style="position:absolute;left:135px;top:62px;width:62px;font-size:2.8px;font-weight:700">Project name<p class="tiny" style="font-weight:400">Lorem ipsum dolor sit amet, nec an dictas equidem appellantur.</p></div>
  <div style="position:absolute;left:135px;top:86px;width:62px;font-size:2.8px;font-weight:700">Project name<p class="tiny" style="font-weight:400">Lorem ipsum dolor sit amet, nec an dictas equidem appellantur.</p></div>
  <div class="footer">COPYRIGHT © 2021 | Ravlo Drive Systems</div><div class="footer-num">15</div>
</section>

<!-- 16: four photo cards -->
<section class="slide c1 r6">
  <div class="brand corner">Ravlo</div>
  <div class="slide-title">Here Goes Title Of This Slide</div>
  <div class="slide-sub">HERE IS A PLACE FOR SUBTITLE</div><div class="title-rule"></div>
  <div style="position:absolute;left:23px;top:33px;width:182px;display:flex;justify-content:space-between">
    <div style="width:40px;text-align:center"><div role="img" aria-label="Photo of a businessman signing papers" style="height:57px;background:linear-gradient(#3a3a3a,#cfcfcf)"></div><div style="height:6px;background:var(--blue);color:#fff;font-size:2.6px;font-weight:600;line-height:6px">Here Goes Title</div><p class="tiny" style="margin-top:3px">We run a fully electric fleet today.</p></div>
    <div style="width:40px;text-align:center"><div role="img" aria-label="Photo of a businessman signing papers" style="height:57px;background:linear-gradient(#3a3a3a,#cfcfcf)"></div><div style="height:6px;background:var(--blue);color:#fff;font-size:2.6px;font-weight:600;line-height:6px">Here Goes Title</div><p class="tiny" style="margin-top:3px">We keep our word to the highest standard.</p></div>
    <div style="width:40px;text-align:center"><div role="img" aria-label="Photo of a businessman signing papers" style="height:57px;background:linear-gradient(#3a3a3a,#cfcfcf)"></div><div style="height:6px;background:var(--blue);color:#fff;font-size:2.6px;font-weight:600;line-height:6px">Here Goes Title</div><p class="tiny" style="margin-top:3px">We hire long term and train well above par.</p></div>
    <div style="width:40px;text-align:center"><div role="img" aria-label="Photo of a businessman signing papers" style="height:57px;background:linear-gradient(#3a3a3a,#cfcfcf)"></div><div style="height:6px;background:var(--blue);color:#fff;font-size:2.6px;font-weight:600;line-height:6px">Here Goes Title</div><p class="tiny" style="margin-top:3px">We live a customer first mindset daily.</p></div>
  </div>
  <div class="footer">COPYRIGHT © 2021 | Ravlo Drive Systems</div><div class="footer-num">16</div>
</section>

<!-- 17: Q&A -->
<section class="slide c2 r6">
  <div class="brand corner">Ravlo</div>
  <div class="slide-title">Here Goes Title Of This Slide</div>
  <div class="slide-sub">HERE IS A PLACE FOR SUBTITLE</div><div class="title-rule"></div>
  <svg width="226" height="125" viewBox="0 0 226 125" style="position:absolute;left:0;top:0" font-family="Montserrat, sans-serif">
    <g font-size="7" font-weight="700" fill="#fff" text-anchor="middle">
      <rect x="23" y="33" width="13" height="13" rx="2" fill="#0b6fc2"/><text x="29.5" y="42.5">Q</text>
      <rect x="23" y="51" width="13" height="13" rx="2" fill="#0b6fc2"/><text x="29.5" y="60.5">Q</text>
      <rect x="23" y="70" width="13" height="13" rx="2" fill="#0b6fc2"/><text x="29.5" y="79.5">Q</text>
      <rect x="23" y="88" width="13" height="13" rx="2" fill="#0b6fc2"/><text x="29.5" y="97.5">Q</text>
      <rect x="127" y="33" width="13" height="13" rx="2" fill="#555"/><text x="133.5" y="42.5">A</text>
      <rect x="127" y="51" width="13" height="13" rx="2" fill="#555"/><text x="133.5" y="60.5">A</text>
      <rect x="127" y="70" width="13" height="13" rx="2" fill="#555"/><text x="133.5" y="79.5">A</text>
      <rect x="127" y="88" width="13" height="13" rx="2" fill="#555"/><text x="133.5" y="97.5">A</text>
    </g>
    <g font-size="2.8" fill="#6d6d6d">
      <text x="42" y="37">Lorem Ipsum is simply dummy</text><text x="42" y="40.5">unknown printer took a galley of</text><text x="42" y="44">type and scrambled it to make.</text>
      <text x="42" y="55">Lorem Ipsum is simply dummy</text><text x="42" y="58.5">unknown printer took a galley of</text><text x="42" y="62">type and scrambled it to make.</text>
      <text x="42" y="74">Lorem Ipsum is simply dummy</text><text x="42" y="77.5">unknown printer took a galley of</text><text x="42" y="81">type and scrambled it to make.</text>
      <text x="42" y="92">Lorem Ipsum is simply dummy</text><text x="42" y="95.5">unknown printer took a galley of</text><text x="42" y="99">type and scrambled it to make.</text>
      <text x="146" y="37">Lorem Ipsum is simply dummy</text><text x="146" y="40.5">unknown printer took a galley of</text><text x="146" y="44">type and scrambled it to make.</text>
      <text x="146" y="55">Lorem Ipsum is simply dummy</text><text x="146" y="58.5">unknown printer took a galley of</text><text x="146" y="62">type and scrambled it to make.</text>
      <text x="146" y="74">Lorem Ipsum is simply dummy</text><text x="146" y="77.5">unknown printer took a galley of</text><text x="146" y="81">type and scrambled it to make.</text>
      <text x="146" y="92">Lorem Ipsum is simply dummy</text><text x="146" y="95.5">unknown printer took a galley of</text><text x="146" y="99">type and scrambled it to make.</text>
    </g>
  </svg>
  <div class="footer">COPYRIGHT © 2021 | Ravlo Drive Systems</div><div class="footer-num">17</div>
</section>

<!-- 18: four-column table -->
<section class="slide c3 r6">
  <div class="brand corner">Ravlo</div>
  <div class="slide-title">Here Goes Title Of This Slide</div>
  <div class="slide-sub">HERE IS A PLACE FOR SUBTITLE</div><div class="title-rule"></div>
  <div style="position:absolute;left:20px;top:36px;width:186px;height:64px;display:flex;font-size:2.8px">
    <div style="flex:1;background:#f0f0f0"><div style="height:11px;background:var(--grey-mid);color:#fff;font-weight:700;text-align:center;line-height:11px">ADD YOUR TITLE</div><div style="padding:4px 5px;font-weight:700">Project name<p class="tiny" style="font-weight:400">Lorem ipsum is simply dummy text of type and scrambled.</p></div><div style="padding:0 5px;font-weight:700">Project name<p class="tiny" style="font-weight:400">Lorem ipsum is simply dummy text of type and scrambled.</p></div></div>
    <div style="flex:1;background:#f7f7f7"><div style="height:11px;background:var(--grey-mid);color:#fff;font-weight:700;text-align:center;line-height:11px">ADD YOUR TITLE</div><div style="padding:4px 5px;font-weight:700">Project name<p class="tiny" style="font-weight:400">Lorem ipsum is simply dummy text of type and scrambled.</p></div><div style="padding:0 5px;font-weight:700">Project name<p class="tiny" style="font-weight:400">Lorem ipsum is simply dummy text of type and scrambled.</p></div></div>
    <div style="flex:1;background:#e3eef9"><div style="height:11px;background:var(--blue);color:#fff;font-weight:700;text-align:center;line-height:11px">ADD YOUR TITLE</div><div style="padding:4px 5px;font-weight:700">Project name<p class="tiny" style="font-weight:400">Lorem ipsum is simply dummy text of type and scrambled.</p></div><div style="padding:0 5px;font-weight:700">Project name<p class="tiny" style="font-weight:400">Lorem ipsum is simply dummy text of type and scrambled.</p></div></div>
    <div style="flex:1;background:#f0f0f0"><div style="height:11px;background:var(--grey-mid);color:#fff;font-weight:700;text-align:center;line-height:11px">ADD YOUR TITLE</div><div style="padding:4px 5px;font-weight:700">Project name<p class="tiny" style="font-weight:400">Lorem ipsum is simply dummy text of type and scrambled.</p></div><div style="padding:0 5px;font-weight:700">Project name<p class="tiny" style="font-weight:400">Lorem ipsum is simply dummy text of type and scrambled.</p></div></div>
  </div>
  <div class="footer">COPYRIGHT © 2021 | Ravlo Drive Systems</div><div class="footer-num">18</div>
</section>

<!-- 19: steps -->
<section class="slide c1 r7">
  <div class="brand corner">Ravlo</div>
  <div class="slide-title">Here Goes Title Of This Slide</div>
  <div class="slide-sub">HERE IS A PLACE FOR SUBTITLE</div><div class="title-rule"></div>
  <svg width="226" height="125" viewBox="0 0 226 125" style="position:absolute;left:0;top:0" font-family="Montserrat, sans-serif">
    <polygon points="18,58 52,58 60,70 52,82 18,82 26,70" fill="#0b6fc2"/>
    <polygon points="55,58 89,58 97,70 89,82 55,82 63,70" fill="#5b5b5b"/>
    <polygon points="92,58 126,58 134,70 126,82 92,82 100,70" fill="#0b6fc2"/>
    <polygon points="129,58 163,58 171,70 163,82 129,82 137,70" fill="#5b5b5b"/>
    <polygon points="166,58 200,58 208,70 200,82 166,82 174,70" fill="#0b6fc2"/>
    <g fill="#fff" text-anchor="middle" font-weight="600">
      <text x="39" y="68" font-size="3.5">STEP</text><text x="39" y="77" font-size="8">01</text>
      <text x="76" y="68" font-size="3.5">STEP</text><text x="76" y="77" font-size="8">02</text>
      <text x="113" y="68" font-size="3.5">STEP</text><text x="113" y="77" font-size="8">03</text>
      <text x="150" y="68" font-size="3.5">STEP</text><text x="150" y="77" font-size="8">04</text>
      <text x="187" y="68" font-size="3.5">STEP</text><text x="187" y="77" font-size="8">05</text>
    </g>
    <g font-size="2.6" fill="#6d6d6d" text-anchor="middle">
      <text x="76" y="36" font-weight="700" fill="#333">Project name</text><text x="76" y="40">Lorem ipsum dolor sit</text><text x="76" y="43.5">nec an dictas equidem</text><text x="76" y="47">appellantur, ut has</text>
      <text x="150" y="36" font-weight="700" fill="#333">Project name</text><text x="150" y="40">Lorem ipsum dolor sit</text><text x="150" y="43.5">nec an dictas equidem</text><text x="150" y="47">appellantur, ut has</text>
      <text x="39" y="91" font-weight="700" fill="#333">Project name</text><text x="39" y="95">Lorem ipsum dolor sit</text><text x="39" y="98.5">nec an dictas equidem</text><text x="39" y="102">appellantur, ut has</text>
      <text x="113" y="91" font-weight="700" fill="#333">Project name</text><text x="113" y="95">Lorem ipsum dolor sit</text><text x="113" y="98.5">nec an dictas equidem</text><text x="113" y="102">appellantur, ut has</text>
      <text x="187" y="91" font-weight="700" fill="#333">Project name</text><text x="187" y="95">Lorem ipsum dolor sit</text><text x="187" y="98.5">nec an dictas equidem</text><text x="187" y="102">appellantur, ut has</text>
    </g>
  </svg>
  <div class="footer">COPYRIGHT © 2021 | Ravlo Drive Systems</div><div class="footer-num">19</div>
</section>

<!-- 20: timeline -->
<section class="slide c2 r7">
  <div class="brand corner">Ravlo</div>
  <div class="slide-title">Here Goes Title Of This Slide</div>
  <div class="slide-sub">HERE IS A PLACE FOR SUBTITLE</div><div class="title-rule"></div>
  <svg width="226" height="125" viewBox="0 0 226 125" style="position:absolute;left:0;top:0" font-family="Montserrat, sans-serif">
    <polygon points="23,64 61,64 58,71 20,71" fill="#0b6fc2"/>
    <polygon points="62,64 100,64 97,71 59,71" fill="#5b5b5b"/>
    <polygon points="101,64 139,64 136,71 98,71" fill="#0b6fc2"/>
    <polygon points="140,64 178,64 175,71 137,71" fill="#5b5b5b"/>
    <polygon points="179,64 217,64 214,71 176,71" fill="#0b6fc2"/>
    <g font-size="3" font-weight="700" fill="#fff" text-anchor="middle">
      <text x="40" y="69">1990</text><text x="79" y="69">2001</text><text x="118" y="69">2007</text><text x="157" y="69">2012</text><text x="196" y="69">2020</text>
    </g>
    <g stroke="#999" stroke-width=".5"><line x1="40" y1="52" x2="40" y2="62"/><line x1="118" y1="52" x2="118" y2="62"/><line x1="196" y1="52" x2="196" y2="62"/><line x1="79" y1="73" x2="79" y2="82"/><line x1="157" y1="73" x2="157" y2="82"/></g>
    <g font-size="2.8" fill="#6d6d6d" text-anchor="middle">
      <text x="40" y="42" fill="#0b6fc2" font-weight="700">Your Title</text><text x="40" y="45.5">Refers to a good or</text><text x="40" y="49">service being offered</text>
      <text x="118" y="42" fill="#0b6fc2" font-weight="700">Your Title</text><text x="118" y="45.5">Refers to a good or</text><text x="118" y="49">service being offered</text>
      <text x="196" y="42" fill="#0b6fc2" font-weight="700">Your Title</text><text x="196" y="45.5">Refers to a good or</text><text x="196" y="49">service being offered</text>
      <text x="79" y="88" font-weight="700" fill="#333">Your Title</text><text x="79" y="91.5">Refers to a good or</text><text x="79" y="95">service being offered</text>
      <text x="157" y="88" font-weight="700" fill="#333">Your Title</text><text x="157" y="91.5">Refers to a good or</text><text x="157" y="95">service being offered</text>
    </g>
  </svg>
  <div class="footer">COPYRIGHT © 2021 | Ravlo Drive Systems</div><div class="footer-num">20</div>
</section>

<!-- 21: cycle diagram -->
<section class="slide c3 r7">
  <div class="brand corner">Ravlo</div>
  <div class="slide-title">Here Goes Title Of This Slide</div>
  <div class="slide-sub">HERE IS A PLACE FOR SUBTITLE</div><div class="title-rule"></div>
  <svg width="226" height="125" viewBox="0 0 226 125" style="position:absolute;left:0;top:0" font-family="Montserrat, sans-serif">
    <g fill="none" stroke-width="14" transform="rotate(-90 113 70)">
      <circle cx="113" cy="70" r="28" stroke="#0b6fc2" stroke-dasharray="43 133"/>
      <circle cx="113" cy="70" r="28" stroke="#5b5b5b" stroke-dasharray="43 133" stroke-dashoffset="-44"/>
      <circle cx="113" cy="70" r="28" stroke="#0b6fc2" stroke-dasharray="43 133" stroke-dashoffset="-88"/>
      <circle cx="113" cy="70" r="28" stroke="#5b5b5b" stroke-dasharray="43 133" stroke-dashoffset="-132"/>
    </g>
    <text x="113" y="72" text-anchor="middle" font-size="8" font-weight="800" fill="#0b6fc2">Ravlo</text>
    <g font-size="2.8" fill="#6d6d6d">
      <text x="55" y="42" font-weight="700" fill="#333">Your Contents Here</text><text x="30" y="47">Lorem ipsum dolor sit amet, consectetur</text><text x="30" y="50.5">adipiscing elit, sed do eiusmod tempor.</text>
      <text x="55" y="82" font-weight="700" fill="#333">Your Contents Here</text><text x="30" y="87">Lorem ipsum dolor sit amet, consectetur</text><text x="30" y="90.5">adipiscing elit, sed do eiusmod tempor.</text>
      <text x="156" y="42" font-weight="700" fill="#333">Your Contents Here</text><text x="156" y="47">Lorem ipsum dolor sit amet, consectetur</text><text x="156" y="50.5">adipiscing elit, sed do eiusmod tempor.</text>
      <text x="156" y="82" font-weight="700" fill="#333">Your Contents Here</text><text x="156" y="87">Lorem ipsum dolor sit amet, consectetur</text><text x="156" y="90.5">adipiscing elit, sed do eiusmod tempor.</text>
    </g>
  </svg>
  <div class="footer">COPYRIGHT © 2021 | Ravlo Drive Systems</div><div class="footer-num">21</div>
</section>

<!-- 22: data table -->
<section class="slide c1 r8">
  <div class="brand corner">Ravlo</div>
  <div class="slide-title">Here Goes Title Of This Slide</div>
  <div class="slide-sub">HERE IS A PLACE FOR SUBTITLE</div><div class="title-rule"></div>
  <svg width="226" height="125" viewBox="0 0 226 125" style="position:absolute;left:0;top:0" font-family="Montserrat, sans-serif">
    <rect x="74" y="31" width="137" height="10" fill="#0b6fc2"/>
    <rect x="17" y="41" width="57" height="70" fill="#5b5b5b"/>
    <g font-size="2.8" font-weight="700" fill="#fff" text-anchor="middle"><text x="91" y="37">Your Text Here</text><text x="125" y="37">Your Text Here</text><text x="159" y="37">Your Text Here</text><text x="193" y="37">Your Text Here</text></g>
    <g font-size="2.8" font-weight="600" fill="#fff"><text x="24" y="47.5">You can replace this text</text><text x="24" y="57.5">You can replace this text</text><text x="24" y="67.5">You can replace this text</text><text x="24" y="77.5">You can replace this text</text><text x="24" y="87.5">You can replace this text</text><text x="24" y="97.5">You can replace this text</text><text x="24" y="107.5">You can replace this text</text></g>
    <g stroke="#e0e0e0" stroke-width=".4"><line x1="74" y1="51" x2="211" y2="51"/><line x1="74" y1="61" x2="211" y2="61"/><line x1="74" y1="71" x2="211" y2="71"/><line x1="74" y1="81" x2="211" y2="81"/><line x1="74" y1="91" x2="211" y2="91"/><line x1="74" y1="101" x2="211" y2="101"/></g>
    <g font-size="3.4" fill="#333" text-anchor="middle">
      <text x="91" y="48">1250</text><text x="91" y="58">3623</text><text x="91" y="68">2569</text><text x="91" y="78">1020</text><text x="91" y="88">2320</text><text x="91" y="98">5698</text><text x="91" y="108">1999</text>
      <text x="159" y="48">50%</text><text x="159" y="58">50%</text><text x="159" y="68">12%</text><text x="159" y="78">65%</text><text x="159" y="88">36%</text><text x="159" y="98">95%</text><text x="159" y="108">66%</text>
      <text x="193" y="48">1250</text><text x="193" y="58">3623</text><text x="193" y="68">2569</text><text x="193" y="78">1020</text><text x="193" y="88">2320</text><text x="193" y="98">5698</text>
    </g>
    <g fill="none" stroke="#0b6fc2" stroke-width="1">
      <polyline points="122,45 124,47 128,43"/><polyline points="122,65 124,67 128,63"/><polyline points="122,85 124,87 128,83"/>
    </g>
    <g stroke="#0a3d73" stroke-width="1"><path d="M123,55 l4,4 m0,-4 l-4,4"/><path d="M123,75 l4,4 m0,-4 l-4,4"/><path d="M123,95 l4,4 m0,-4 l-4,4"/><path d="M123,105 l4,4 m0,-4 l-4,4"/></g>
  </svg>
  <div class="footer">COPYRIGHT © 2021 | Ravlo Drive Systems</div><div class="footer-num">22</div>
</section>

<!-- 23: nested circles -->
<section class="slide c2 r8">
  <div class="brand corner">Ravlo</div>
  <div class="slide-title">Here Goes Title Of This Slide</div>
  <div class="slide-sub">HERE IS A PLACE FOR SUBTITLE</div><div class="title-rule"></div>
  <svg width="226" height="125" viewBox="0 0 226 125" style="position:absolute;left:0;top:0" font-family="Montserrat, sans-serif">
    <circle cx="51" cy="71" r="34" fill="#0b6fc2"/>
    <circle cx="51" cy="80" r="25" fill="#1da6ea"/>
    <circle cx="51" cy="92" r="13" fill="#5b5b5b"/>
    <g fill="#fff" font-weight="700" text-anchor="middle"><text x="51" y="50" font-size="7">$</text><text x="51" y="72" font-size="6">$</text><text x="51" y="95" font-size="5">$</text></g>
    <g stroke="#5b5b5b" stroke-width=".4"><line x1="51" y1="48" x2="92" y2="48"/><line x1="51" y1="70" x2="92" y2="70"/><line x1="51" y1="93" x2="92" y2="93"/></g>
    <g font-size="6" font-weight="600" fill="#333"><text x="94" y="50">999M</text><text x="94" y="72">99M</text><text x="94" y="95">9M</text></g>
    <g fill="none" stroke-width="1.6"><polyline points="138,48 141,51 147,44" stroke="#0b6fc2"/><polyline points="138,70 141,73 147,66" stroke="#1da6ea"/><polyline points="138,93 141,96 147,89" stroke="#5b5b5b"/></g>
    <g font-size="2.8" fill="#6d6d6d">
      <text x="154" y="44" font-weight="700" fill="#333">Lorem ipsum dolor</text><text x="154" y="48">Lorem ipsum dolor sit amet,</text><text x="154" y="51.5">consectetur adipiscing elit.</text>
      <text x="154" y="66" font-weight="700" fill="#333">Lorem ipsum dolor</text><text x="154" y="70">Lorem ipsum dolor sit amet,</text><text x="154" y="73.5">consectetur adipiscing elit.</text>
      <text x="154" y="89" font-weight="700" fill="#333">Lorem ipsum dolor</text><text x="154" y="93">Lorem ipsum dolor sit amet,</text><text x="154" y="96.5">consectetur adipiscing elit.</text>
    </g>
  </svg>
  <div class="footer">COPYRIGHT © 2021 | Ravlo Drive Systems</div><div class="footer-num">23</div>
</section>

<!-- 24: donut percentages -->
<section class="slide c3 r8">
  <div class="brand corner">Ravlo</div>
  <div class="slide-title">Here Goes Title Of This Slide</div>
  <div class="slide-sub">HERE IS A PLACE FOR SUBTITLE</div><div class="title-rule"></div>
  <svg width="226" height="125" viewBox="0 0 226 125" style="position:absolute;left:0;top:0" font-family="Montserrat, sans-serif">
    <g font-size="2.8" fill="#0b6fc2" text-anchor="middle"><text x="113" y="35">Lorem ipsum the printing and typesetting industry, the standard dummy text</text><text x="113" y="39">ever since the 1500s, when an unknown printer took a galley of type and</text><text x="113" y="43">scrambled it to make a type specimen book that has survived.</text></g>
    <g fill="none" stroke-width="2.4">
      <circle cx="66" cy="73" r="15" stroke="#0b6fc2" stroke-dasharray="47 94" transform="rotate(-90 66 73)"/>
      <circle cx="113" cy="73" r="15" stroke="#1da6ea" stroke-dasharray="70.7 94" transform="rotate(-90 113 73)"/>
      <circle cx="160" cy="73" r="15" stroke="#5b5b5b" stroke-dasharray="37.7 94" transform="rotate(-90 160 73)"/>
    </g>
    <g font-size="7" font-weight="600" text-anchor="middle"><text x="66" y="76" fill="#0b6fc2">50%</text><text x="113" y="76" fill="#1da6ea">75%</text><text x="160" y="76" fill="#5b5b5b">40%</text></g>
    <g font-size="2.8" fill="#6d6d6d" text-anchor="middle"><text x="66" y="97">Lorem ipsum dolor amet</text><text x="66" y="100.5">amet consectetur dolor</text><text x="113" y="97">Lorem ipsum dolor amet</text><text x="113" y="100.5">amet consectetur dolor</text><text x="160" y="97">Lorem ipsum dolor amet</text><text x="160" y="100.5">amet consectetur dolor</text></g>
  </svg>
  <div class="footer">COPYRIGHT © 2021 | Ravlo Drive Systems</div><div class="footer-num">24</div>
</section>

<!-- 25: contact -->
<section class="slide c1 r9">
  <div class="photo" role="img" aria-label="Blue tinted photo of a hand pointing" style="inset:0;background:linear-gradient(120deg,#0a4e99,#2a7fd0 60%,#a9c4e2)"></div>
  <div class="brand light" style="left:46px;top:20px">Ravlo</div>
  <div style="position:absolute;left:31px;top:33px;width:61px;font-size:2.8px;color:var(--grey)">
    <div style="height:14px;background:#fff;margin-bottom:2px;padding:5px 0 0 15px;position:relative"><span style="position:absolute;left:5px;top:4px;width:5px;height:5px;border:.6px solid var(--blue);border-radius:50%"></span>www.ravlo.example</div>
    <div style="height:14px;background:#fff;margin-bottom:2px;padding:3.5px 0 0 15px;position:relative;line-height:1.2"><svg width="5" height="6" viewBox="0 0 10 12" style="position:absolute;left:5px;top:4px"><path d="M5 12 C1 7 0 5 0 4 A5 5 0 0 1 10 4 C10 5 9 7 5 12Z" fill="#0b6fc2"/></svg>Here to write your<br>Company adress</div>
    <div style="height:14px;background:#fff;margin-bottom:2px;padding:5px 0 0 15px;position:relative"><svg width="5" height="5" viewBox="0 0 10 10" style="position:absolute;left:5px;top:4.5px"><path d="M2 0 L4 3 L3 4 Q4 6 6 7 L7 6 L10 8 L8 10 Q0 8 0 2Z" fill="#0b6fc2"/></svg>(555) 014-2290</div>
    <div style="height:14px;background:#fff;padding:5px 0 0 15px;position:relative"><svg width="5" height="4" viewBox="0 0 10 8" style="position:absolute;left:5px;top:5px"><rect width="10" height="8" fill="#0b6fc2"/><polyline points="0,0 5,4 10,0" fill="none" stroke="#fff" stroke-width="1"/></svg>hello@ravlo.example</div>
  </div>
  <div class="social" style="left:45px;top:101px"><i></i><i></i><i></i><i></i></div>
  <div style="position:absolute;left:125px;top:55px;font-size:8px;font-weight:700;color:var(--white)">CONTACT US</div>
  <div style="position:absolute;left:129px;top:66px;font-size:7px;font-weight:400;color:var(--white)">Get in touch</div>
</section>

<!-- 26: compare products -->
<section class="slide c2 r9">
  <div class="slide-title">Compare Our Products</div>
  <div class="slide-sub">HERE IS A PLACE FOR SUBTITLE</div><div class="title-rule"></div>
  <svg width="226" height="125" viewBox="0 0 226 125" style="position:absolute;left:0;top:0" font-family="Montserrat, sans-serif">
    <rect x="15" y="40" width="45" height="60" fill="#f3f3f3" stroke="#ddd" stroke-width=".4"/><rect x="15" y="40" width="45" height="6" fill="#5b5b5b"/>
    <rect x="63" y="40" width="34" height="60" fill="#fff" stroke="#ddd" stroke-width=".4"/><rect x="63" y="40" width="34" height="6" fill="#0b6fc2"/>
    <rect x="100" y="40" width="34" height="60" fill="#fff" stroke="#ddd" stroke-width=".4"/><rect x="100" y="40" width="34" height="6" fill="#5b5b5b"/>
    <rect x="137" y="40" width="34" height="60" fill="#fff" stroke="#ddd" stroke-width=".4"/><rect x="137" y="40" width="34" height="6" fill="#5b5b5b"/>
    <rect x="174" y="40" width="34" height="60" fill="#fff" stroke="#ddd" stroke-width=".4"/><rect x="174" y="40" width="34" height="6" fill="#5b5b5b"/>
    <g font-size="2.4" font-weight="700" fill="#fff" text-anchor="middle"><text x="37.5" y="44">Product Name Or Feature</text><text x="80" y="44">Ravlo</text><text x="117" y="44">Competitor No. 1</text><text x="154" y="44">Competitor No. 2</text><text x="191" y="44">Competitor No. 3</text></g>
    <g font-size="2.4" fill="#6d6d6d"><text x="20" y="53">You can replace this text</text><text x="20" y="60">You can replace this text</text><text x="20" y="67">You can replace this text</text><text x="20" y="74">You can replace this text</text><text x="20" y="81">You can replace this text</text><text x="20" y="88">You can replace this text</text><text x="20" y="95">You can replace this text</text></g>
    <g fill="none" stroke="#0b6fc2" stroke-width=".8">
      <path d="M78,51.5l1.5,1.5l3,-3 M78,58.5l1.5,1.5l3,-3 M78,65.5l1.5,1.5l3,-3 M78,72.5l1.5,1.5l3,-3 M78,79.5l1.5,1.5l3,-3 M78,86.5l1.5,1.5l3,-3 M78,93.5l1.5,1.5l3,-3"/>
      <path d="M152,51.5l1.5,1.5l3,-3 M152,65.5l1.5,1.5l3,-3 M152,79.5l1.5,1.5l3,-3 M152,86.5l1.5,1.5l3,-3 M115,58.5l1.5,1.5l3,-3 M115,72.5l1.5,1.5l3,-3 M115,86.5l1.5,1.5l3,-3 M189,58.5l1.5,1.5l3,-3 M189,79.5l1.5,1.5l3,-3 M189,86.5l1.5,1.5l3,-3"/>
    </g>
    <g stroke="#0a3d73" stroke-width=".8">
      <path d="M115.5,50l3,3m0,-3l-3,3 M115.5,64l3,3m0,-3l-3,3 M115.5,78l3,3m0,-3l-3,3 M115.5,92l3,3m0,-3l-3,3 M152.5,57l3,3m0,-3l-3,3 M152.5,71l3,3m0,-3l-3,3 M152.5,92l3,3m0,-3l-3,3 M189.5,50l3,3m0,-3l-3,3 M189.5,64l3,3m0,-3l-3,3 M189.5,71l3,3m0,-3l-3,3 M189.5,92l3,3m0,-3l-3,3"/>
    </g>
  </svg>
  <div class="footer">COPYRIGHT © 2021 | Ravlo Drive Systems</div><div class="footer-num">26</div>
</section>

<!-- 27: compare with product image -->
<section class="slide c3 r9">
  <div class="slide-title">Compare Our Products</div>
  <div class="slide-sub">HERE IS A PLACE FOR SUBTITLE</div><div class="title-rule"></div>
  <div class="photo" role="img" aria-label="Close-up photo of a timing belt in a round frame" style="left:10px;top:55px;width:47px;height:47px;border-radius:50%;background:linear-gradient(135deg,#8a4d1e,#2a2a2a);border:1px solid var(--blue)"></div>
  <svg width="226" height="125" viewBox="0 0 226 125" style="position:absolute;left:0;top:0" font-family="Montserrat, sans-serif">
    <path d="M52,54 Q56,42 68,42" fill="none" stroke="#0b6fc2" stroke-width=".5" stroke-dasharray="1.2 1"/>
    <rect x="78" y="40" width="42" height="60" fill="#fff" stroke="#ddd" stroke-width=".4"/><rect x="78" y="40" width="42" height="6" fill="#0b6fc2"/>
    <rect x="122" y="40" width="54" height="60" fill="#5b5b5b"/>
    <rect x="179" y="40" width="40" height="60" fill="#fff" stroke="#ddd" stroke-width=".4"/><rect x="179" y="40" width="40" height="6" fill="#5b5b5b"/>
    <g font-size="2.4" font-weight="700" fill="#fff" text-anchor="middle"><text x="99" y="44">Ravlo</text><text x="149" y="44">Product Name Or Feature</text><text x="199" y="44">Competitor No. 1</text></g>
    <g font-size="2.4" fill="#e6e6e6"><text x="128" y="53">You can replace this text</text><text x="128" y="61">You can replace this text</text><text x="128" y="69">You can replace this text</text><text x="128" y="77">You can replace this text</text><text x="128" y="85">You can replace this text</text><text x="128" y="93">You can replace this text</text></g>
    <g fill="none" stroke="#0b6fc2" stroke-width=".8">
      <path d="M97,51.5l1.5,1.5l3,-3 M97,59.5l1.5,1.5l3,-3 M97,67.5l1.5,1.5l3,-3 M97,75.5l1.5,1.5l3,-3 M97,83.5l1.5,1.5l3,-3 M97,91.5l1.5,1.5l3,-3 M197,51.5l1.5,1.5l3,-3 M197,83.5l1.5,1.5l3,-3 M197,91.5l1.5,1.5l3,-3"/>
    </g>
    <g stroke="#0a3d73" stroke-width=".8"><path d="M197.5,58l3,3m0,-3l-3,3 M197.5,66l3,3m0,-3l-3,3 M197.5,74l3,3m0,-3l-3,3"/></g>
  </svg>
  <div class="footer">COPYRIGHT © 2021 | Ravlo Drive Systems</div><div class="footer-num">27</div>
</section>

</body>
</html>
```